Personal Business Card Design Project

I am looking for a business card to be able to hand to both Chinese and Australian businessman.
I am a self employed consultant and just need my name, phone number and email address on the card. No Business Name and No Website.
I want it to look like an exclusive prestigious card.
I would like the background to be be a glossy red and the writing to be gold. (This applies to both sides of the card).
It must have English on one side and Chinese (Mandarin) on the reverse.
Details you will require
Name : Wade Emmerson
Phone : + 61 493 207 158
Email : wadeyemmerson@brightpost.example
Thank you everybody for your designs.
Industry/Entity Type
Business

```html
<!DOCTYPE html>
<html lang="en">
<head>
<meta charset="utf-8">
<title>Wade Emmerson – Consultant</title>
<link rel="stylesheet" href="https://fonts.googleapis.com/css2?family=Yellowtail&display=swap">
<style>
  :root {
    --red-top: #ff0303;
    --red-bottom: #990000;
    --frame: #0a0000;
    --ornament-fill: #6e0000;
    --gold-light: #fff27a;
    --gold-mid: #f2c419;
    --gold-deep: #b47a06;
    --ink: #0a0000;
  }
  html, body {
    margin: 0;
    padding: 0;
    overflow: hidden;
    background: #ffffff;
  }
  .card {
    position: relative;
    width: 1200px;
    height: 700px;
    overflow: hidden;
    background: linear-gradient(to bottom, var(--red-top) 0%, #d00000 50%, var(--red-bottom) 100%);
    font-family: "Yellowtail", cursive;
  }
  .card__frame {
    position: absolute;
    inset: 0;
    width: 1200px;
    height: 700px;
  }
  .frame-line { fill: var(--frame); }
  .frame-ornament { fill: var(--ornament-fill); }

  .card__text {
    position: absolute;
    margin: 0;
    white-space: nowrap;
    line-height: 1;
  }
  .card__name {
    left: 122px;
    top: 128px;
    font-size: 72px;
    letter-spacing: 1px;
    background: linear-gradient(to bottom, var(--gold-light) 0%, var(--gold-mid) 50%, var(--gold-deep) 100%);
    -webkit-background-clip: text;
    background-clip: text;
    color: transparent;
    filter: drop-shadow(2px 3px 1px rgba(60, 0, 0, 0.7));
  }
  .card__role {
    left: 190px;
    top: 212px;
    font-size: 62px;
    color: var(--ink);
    letter-spacing: 1px;
  }
  .card__contact {
    color: var(--gold-mid);
    -webkit-text-stroke: 4px var(--ink);
    paint-order: stroke fill;
    background: none;
  }
  .card__phone {
    left: 150px;
    top: 395px;
    font-size: 64px;
    letter-spacing: 3px;
  }
  .card__email {
    left: 154px;
    top: 478px;
    font-size: 50px;
    letter-spacing: 1px;
  }
</style>
</head>
<body>
  <div class="card">
    <svg class="card__frame" viewBox="0 0 1260 735" preserveAspectRatio="none" aria-hidden="true">
      <defs>
        <g id="corner">
          <!-- outer thin bracket -->
          <rect class="frame-line" x="28" y="0" width="8" height="322"/>
          <rect class="frame-line" x="0" y="28" width="320" height="8"/>
          <!-- corner square -->
          <rect class="frame-line" x="0" y="0" width="36" height="36"/>
          <rect x="6" y="6" width="22" height="22" fill="#e00000"/>
          <!-- inner heavy bracket -->
          <rect class="frame-line" x="44" y="44" width="12" height="278"/>
          <rect class="frame-line" x="44" y="44" width="276" height="12"/>
        </g>
        <path id="corner-ornament" d="M60 60 H225 Q120 80 66 225 L60 225 Z"/>
      </defs>

      <use href="#corner"/>
      <use href="#corner" transform="translate(1260 0) scale(-1 1)"/>
      <use href="#corner" transform="translate(0 735) scale(1 -1)"/>
      <use href="#corner" transform="translate(1260 735) scale(-1 -1)"/>

      <g class="frame-ornament">
        <use href="#corner-ornament" role="img" aria-label="Decorative scroll flourish, top left"/>
        <use href="#corner-ornament" transform="translate(1260 0) scale(-1 1)" role="img" aria-label="Decorative scroll flourish, top right"/>
        <use href="#corner-ornament" transform="translate(0 735) scale(1 -1)" role="img" aria-label="Decorative scroll flourish, bottom left"/>
        <use href="#corner-ornament" transform="translate(1260 735) scale(-1 -1)" role="img" aria-label="Decorative scroll flourish, bottom right"/>
      </g>
    </svg>

    <h1 class="card__text card__name">Wade Emmerson</h1>
    <p class="card__text card__role">Consultant</p>
    <p class="card__text card__contact card__phone">+ 61 493 207 158</p>
    <p class="card__text card__contact card__email">wadeyemmerson@brightpost.example</p>
  </div>
</body>
</html>
```